Gordon Pellbrook Consulting - Web Design Project

We need a web design for my new edgy consulting business specializing in innovation, technology and strategy.

It is our personal goal to turn each client into raving fans by helping them achieve their own business goals and aspirations through assisting them in raising their own innovation and marketing standards.

We provide our personalised and state-of-the-art services to our clients and boards who represent some of the world greatest innovative thinkers.
Updates

Here is some other information which may help shape your thinking.

I've had direct Involvement in the development of the following iPad, iPhone Applications and websites

FarbeyondOzlands.com (TerraLink platform) by Voyage Bureau
http://farbeyondozlands.example.au

Sail Verve by Bright Voyaging
https://apps.example-store.com/au/app/sail-verve/id100000001

uRedlandTR by Travel Territory Board
https://apps.example-store.com/au/app/uredlandtr/id100000002

Wexmoor Trips
http://www.wexmoortrips.example.au

Trek Mapper by Voyage Bureau
http://apps.example-store.com/au/app/trek-mapper/id100000003

Sunward by Sunward Travel Office
https://apps.example-store.com/au/app/sunward/id100000004

Upper Fernridge Valley Route by Visit Coastlands
https://apps.example-store.com/au/app/upper-fernridge-valley-route/id100000005

Wanderer Path by Travel Territory Board and Southern Plains Travel Council
https://apps.example-store.com/au/app/wanderers-path-grand-journey/id100000006

Gordon Pellbrook Consulting (GPC)
November 2012 – Present (8 months)Brisbane, Sydney, Canberra

Gordon’s consults to Small-to-Medium Enterprises (SME) and Government organisations on business strategy, technology strategy, risk mitigation, disruptive technology and innovation in the workplace.

Gordon’s consultancy mantra is that we cannot divorce economic life from cultural life particularly in an era when social capital may be as important as physical capital in business.

Reason: request from designers, I want to see their best efforts

Target Market(s)

35+

Industry/Entity Type

Business

Requirements
Must have
• Please use some of the personal image(s) contained in the zip files which can be downloaded from here

http://filedrop.example/k9Xq2Lm
http://filedrop.example/p4Rt7Vn
http://filedrop.example/z8Hw3Bc
Nice to have
• Black, Sleek design, maybe minimalist. Nice to have a Pixelle for the design. Nice to have it easily ported to Wordpress or be a modified Wordpress template. HTML 5, responsive design

```html
<!DOCTYPE html>
<html lang="en">
<head>
<meta charset="utf-8">
<title>Gordon Pellbrook Consulting</title>
<link rel="stylesheet" href="https://fonts.googleapis.com/css2?family=Source+Sans+3:wght@300;400;600;700&display=swap">
<style>
  :root {
    --backdrop: #e4e4e4;
    --page: #f8f8f8;
    --ink: #1f1e22;
    --ink-soft: #6d6d70;
    --nav-active: #3b3a3f;
    --circle-a: #3a3b3d;
    --circle-b: #25232e;
    --circle-c: #555557;
    --button: #2a2724;
    --footer: #232226;
    --field-border: #c9c9c9;
    --social: #6a6468;
  }
  * { box-sizing: border-box; margin: 0; padding: 0; }
  html, body { width: 1200px; height: 1000px; overflow: hidden; }
  body {
    background: var(--backdrop);
    font-family: "Source Sans 3", "Myriad Pro", sans-serif;
    color: var(--ink);
    position: relative;
  }
  .page {
    position: absolute; left: 417px; top: 23px; width: 365px; height: 955px;
    background: var(--page);
    box-shadow: 0 0 3px rgba(0,0,0,.15);
    overflow: hidden;
  }
  .abs { position: absolute; }

  /* navigation */
  .nav-item {
    position: absolute; top: 1px; width: 32px; height: 62px;
    font-size: 6px; line-height: 7px; text-align: center; color: var(--ink);
    padding-top: 25px;
  }
  .nav-item svg { position: absolute; top: 24px; left: 11px; width: 10px; height: 10px; }
  .nav-item span { display: block; margin-top: 17px; }
  .nav-item.is-active { background: var(--nav-active); color: #fff; }
  .nav-item.is-active span { margin-top: 17px; }

  .brand { left: 290px; top: 11px; width: 60px; text-align: center; }
  .brand-name { font-size: 17px; font-weight: 300; letter-spacing: 1px; line-height: 18px; }
  .brand-tag { font-size: 4.5px; line-height: 5px; color: var(--ink-soft); }

  /* hero */
  .hero-scene {
    left: 0; top: 85px; width: 365px; height: 138px;
    background: linear-gradient(90deg, #dfe6e4 0%, #f3f5f4 40%, #e6ecea 100%);
  }
  .hero-portrait {
    left: 201px; top: 52px; width: 164px; height: 171px;
    background: linear-gradient(180deg, #c9a892 0%, #9aa2ab 45%, #6f7a88 100%);
  }
  .hero-copy { left: 45px; top: 116px; font-size: 12px; line-height: 15px; color: #8b8b8b; font-weight: 300; }
  .hero-copy strong { color: var(--ink); font-weight: 600; }
  .hero-signature { left: 110px; top: 183px; width: 92px; height: 14px; background: rgba(80,80,80,.25); border-radius: 7px; }

  /* services */
  .service { top: 251px; width: 80px; text-align: center; }
  .service-circle {
    width: 62px; height: 62px; border-radius: 50%; margin: 0 auto;
    display: flex; align-items: center; justify-content: center;
  }
  .service-label { margin-top: 11px; font-size: 8px; font-weight: 700; }

  .divider {
    left: 20px; width: 325px; height: 6px;
    background: radial-gradient(ellipse at center top, rgba(0,0,0,.14), rgba(0,0,0,0) 70%);
  }

  .sketch { left: 3px; top: 392px; width: 160px; height: 160px;
    background: radial-gradient(ellipse at 50% 50%, #d8d8d8 0%, #ececec 50%, var(--page) 75%); }
  .sketch-figure { left: 58px; top: 410px; width: 42px; height: 140px; background: #2a2a2e; border-radius: 14px 14px 4px 4px; }

  .block-title { font-size: 12px; line-height: 15px; font-weight: 300; }
  .block-title strong { font-weight: 700; }
  .block-body { font-size: 5.5px; line-height: 7px; color: var(--ink); }
  .more {
    width: 44px; height: 13px; background: var(--button); color: #fff;
    font-size: 7px; font-weight: 600; text-align: center; line-height: 13px;
  }

  .goal-art { left: 213px; top: 608px; width: 152px; height: 136px;
    background: linear-gradient(135deg, #e8d6d6 0%, #b06a6a 35%, #2b2b30 70%, #1d1d22 100%); }

  /* contact */
  .map { left: 0; top: 744px; width: 203px; height: 171px;
    background: linear-gradient(135deg, #e8e2d4 0%, #ded9c8 50%, #cfe0c8 100%); }
  .contact { left: 221px; top: 750px; width: 125px; }
  .contact-title { font-size: 12px; font-weight: 300; line-height: 14px; }
  .field-label { font-size: 6.5px; margin-top: 6px; line-height: 8px; }
  .field { margin-top: 1px; height: 13px; border: 1px solid var(--field-border); background: #fff;
    box-shadow: inset 0 1px 2px rgba(0,0,0,.15); width: 121px; }
  .field.is-tall { height: 31px; }
  .submit { margin: 13px 0 0 78px; width: 43px; height: 13px; background: var(--button); color: #fff;
    font-size: 7px; font-weight: 600; text-align: center; line-height: 13px; }

  .footer { left: 0; top: 915px; width: 365px; height: 40px; background: var(--footer); }
  .footer-note { left: 126px; top: 16px; font-size: 5px; color: #bcbcbc; }
  .social { top: 15px; width: 9px; height: 9px; background: var(--social); }
</style>
</head>
<body>
<main class="page">
  <nav>
    <div class="nav-item is-active" style="left:26px">
      <svg viewBox="0 0 10 10"><path d="M5 1 1 5h1.5v4h2V6.5h1V9h2V5H9z" fill="#fff"/></svg>
      <span>Home</span>
    </div>
    <div class="nav-item" style="left:68px">
      <svg viewBox="0 0 10 10"><circle cx="5" cy="3.3" r="2.2" fill="none" stroke="#1f1e22" stroke-width="1.3"/><path d="M1.3 9.3c.4-2.4 1.8-3.4 3.7-3.4s3.3 1 3.7 3.4z" fill="none" stroke="#1f1e22" stroke-width="1.3"/></svg>
      <span>About<br>Us</span>
    </div>
    <div class="nav-item" style="left:113px">
      <svg viewBox="0 0 10 10"><circle cx="4.2" cy="4.2" r="3" fill="none" stroke="#1f1e22" stroke-width="1.3"/><path d="M6.4 6.4 9.2 9.2" stroke="#1f1e22" stroke-width="1.6"/><path d="M4.2 2.8v2.8M2.8 4.2h2.8" stroke="#1f1e22" stroke-width=".9"/></svg>
      <span>Why<br>Choose Us?</span>
    </div>
    <div class="nav-item" style="left:157px">
      <svg viewBox="0 0 10 10"><rect x="1" y="2.2" width="8" height="5.8" fill="none" stroke="#1f1e22" stroke-width="1.2"/><path d="M1 2.4 5 5.6l4-3.2" fill="none" stroke="#1f1e22" stroke-width="1.1"/></svg>
      <span>Contact<br>Us</span>
    </div>
  </nav>

  <div class="abs brand">
    <div class="brand-name">GPC</div>
    <div class="brand-tag">gordon pellbrook<br>consultant</div>
  </div>

  <section>
    <div class="abs hero-scene" role="img" aria-label="Bright office interior with large windows, softly blurred"></div>
    <div class="abs hero-copy">
      We are new edgy<br>
      <strong>Consulting Business</strong><br>
      specializing in innovation,<br>
      technology and strategy.
    </div>
    <div class="abs hero-signature" role="img" aria-label="Handwritten signature of Gordon Pellbrook"></div>
    <div class="abs hero-portrait" role="img" aria-label="Portrait of Gordon Pellbrook in a grey suit jacket"></div>
  </section>

  <section>
    <div class="abs service" style="left:38px">
      <div class="service-circle" style="background:var(--circle-a)">
        <svg width="26" height="26" viewBox="0 0 26 26"><path d="M10 3h6M11 3v7L4.5 21.5c-.6 1 .1 2 1.2 2h14.6c1.1 0 1.8-1 1.2-2L15 10V3" fill="#fff"/><path d="M10 3h6" stroke="#fff" stroke-width="2"/></svg>
      </div>
      <div class="service-label">INNOVATION</div>
    </div>
    <div class="abs service" style="left:147px">
      <div class="service-circle" style="background:var(--circle-b)">
        <svg width="26" height="26" viewBox="0 0 26 26"><rect x="2" y="3" width="22" height="20" rx="1.5" fill="none" stroke="#fff" stroke-width="2.2"/><rect x="2" y="3" width="22" height="5" fill="#fff"/><circle cx="5" cy="5.5" r="1" fill="#25232e"/><circle cx="8" cy="5.5" r="1" fill="#25232e"/><circle cx="11" cy="5.5" r="1" fill="#25232e"/><path d="M11 11v9l2.4-2.3 1.8 3.6 1.6-.8-1.8-3.5H18z" fill="#fff"/></svg>
      </div>
      <div class="service-label">TECHNOLOGY</div>
    </div>
    <div class="abs service" style="left:250px">
      <div class="service-circle" style="background:var(--circle-c)">
        <svg width="28" height="28" viewBox="0 0 28 28"><circle cx="14" cy="14" r="8" fill="none" stroke="#fff" stroke-width="2.6"/><ellipse cx="14" cy="14" rx="13" ry="4.5" transform="rotate(-30 14 14)" fill="none" stroke="#fff" stroke-width="2"/></svg>
      </div>
      <div class="service-label">STRATEGY</div>
    </div>
  </section>

  <div class="abs divider" style="top:377px"></div>

  <section>
    <div class="abs sketch" role="img" aria-label="Hand-drawn business concept sketches with charts and arrows"></div>
    <div class="abs sketch-figure" role="img" aria-label="Gordon Pellbrook standing in a dark suit"></div>
    <div class="abs block-title" style="left:196px;top:432px">
      We provide our<br>personalised and<br>state-of-the-art services
    </div>
    <div class="abs block-body" style="left:196px;top:484px;width:135px">
      to our clients and boards who represent some of the world greatest innovative thinkers.
    </div>
    <div class="abs more" style="left:290px;top:508px">more</div>
  </section>

  <div class="abs divider" style="top:567px"></div>

  <section>
    <div class="abs block-title" style="left:36px;top:605px">
      It is our<br>personal <strong>goal</strong>
    </div>
    <div class="abs block-body" style="left:36px;top:642px;width:137px;text-align:justify">
      to turn each client into raving fans by helping them achieve their own business goals and aspirations through assisting them in raising their own innovation and marketing standards.
    </div>
    <div class="abs more" style="left:131px;top:681px">more</div>
    <div class="abs goal-art" role="img" aria-label="Gordon Pellbrook in a dark suit beside red target rings"></div>
  </section>

  <section>
    <div class="abs map" role="img" aria-label="Street map of the office area with a red location pin"></div>
    <svg class="abs" style="left:81px;top:818px" width="14" height="22" viewBox="0 0 14 22"><path d="M7 1C3.7 1 1 3.6 1 7c0 4.5 6 14 6 14s6-9.5 6-14c0-3.4-2.7-6-6-6z" fill="#d8232a"/><circle cx="7" cy="7" r="2.4" fill="#fff"/></svg>
    <form class="abs contact">
      <div class="contact-title">contact us</div>
      <div class="field-label">Name:</div>
      <div class="field"></div>
      <div class="field-label" style="margin-top:7px">Email</div>
      <div class="field"></div>
      <div class="field-label">Message</div>
      <div class="field is-tall"></div>
      <div class="submit">submit</div>
    </form>
  </section>

  <footer class="abs footer">
    <div class="abs footer-note">Copyright | All Right Reserved 2013 | Terms &amp; Conditions</div>
    <div class="abs social" style="left:277px"></div>
    <div class="abs social" style="left:295px"></div>
    <div class="abs social" style="left:313px"></div>
    <div class="abs social" style="left:331px"></div>
  </footer>
</main>
</body>
</html>
```